Website for Torvane Capital - investment banking firm

We have a corporate identity (thanks to Ravella/48213) and want to extend that into a website design.  See the attached zipped files.
We have software folks in-house to do the coding.
See the attached Project Brief & Notes for more details.  Don't worry about the actual text - lorem ipsum will be fine.
The server will be Apache.
Thank you!
Leopold

```html
<!DOCTYPE html>
<html lang="en">
<head>
<meta charset="utf-8">
<title>Torvane Capital</title>
<link href="https://fonts.googleapis.com/css2?family=Arimo:wght@400;700&family=Raleway:wght@200;300;800&display=swap" rel="stylesheet">
<style>
:root{
  --ink:#1c1c1c;
  --header:#1e1e1e;
  --white:#ffffff;
  --text:#3a3a3a;
  --muted:#6e6e6e;
  --line:#dddddd;
  --hero-a:#8c8c8c;
  --hero-b:#4a4a4a;
  --friendlane:#2a5aa8;
  --circlenet:#e0523f;
  --streamvid:#cc1a1a;
}
*{margin:0;padding:0;box-sizing:border-box}
html,body{width:837px;height:1200px;overflow:hidden;background:var(--white)}
body{position:relative;font-family:Arimo,Helvetica,Arial,sans-serif;color:var(--text)}
.abs{position:absolute}

/* header */
.site-header{position:absolute;left:0;top:0;width:837px;height:84px;background:var(--header)}
.brand{position:absolute;left:127px;top:25px;display:flex;align-items:center;gap:8px;color:var(--white)}
.brand-mark{width:26px;height:26px;border:2px solid var(--white);border-radius:50%}
.brand-name{font-size:17px;letter-spacing:1px;text-transform:uppercase;font-weight:400}
.social-mini{position:absolute;left:372px;top:23px;display:flex;gap:6px;font-size:6.5px;color:var(--white)}
.phone{position:absolute;left:459px;top:22px;display:flex;align-items:center;gap:4px;color:var(--white);font-size:6.5px;font-weight:700}
.phone-dot{width:9px;height:9px;border-radius:50%;background:var(--white)}
.search{position:absolute;left:552px;top:20px;width:158px;height:15px;background:var(--white);border-radius:8px;display:flex;align-items:center;font-size:6px}
.search-input{flex:1;padding-left:7px;color:#999}
.search-btn{width:40px;border-left:1px solid #ccc;height:100%;display:flex;align-items:center;justify-content:center;font-weight:700;color:var(--ink)}
.main-nav{position:absolute;right:127px;top:57px;display:flex;gap:15px;font-size:8px;color:var(--white)}
.main-nav .active{font-weight:700;border-bottom:1px solid var(--white);padding-bottom:1px}

/* hero */
.hero{position:absolute;left:0;top:84px;width:837px;height:217px;background:radial-gradient(ellipse at 50% 40%,var(--hero-a),var(--hero-b))}
.hero-map{position:absolute;left:150px;top:10px;width:570px;height:170px;background:radial-gradient(ellipse at center,rgba(255,255,255,.18),rgba(255,255,255,0) 70%)}
.hero-arrow{position:absolute;top:96px;width:26px;height:26px;background:var(--ink);display:flex;align-items:center;justify-content:center}
.hero-title{position:absolute;left:0;width:837px;text-align:center;color:var(--white);font-family:Raleway,Arimo,sans-serif;line-height:1}
.hero-title .l1{display:block;font-weight:800;font-size:27px;letter-spacing:1px;margin-top:126px}
.hero-title .l2{display:block;font-weight:200;font-size:31px;margin-top:1px}
.hero-dots{position:absolute;left:384px;top:200px;display:flex;gap:2px}
.hero-dots span{width:21px;height:2px;background:var(--ink)}
.hero-dots span.on{background:var(--white)}

/* intro */
.intro{position:absolute;left:150px;top:322px;width:537px;text-align:center;font-size:11.2px;line-height:19.6px;color:var(--text)}

.section-title{position:absolute;left:0;width:837px;text-align:center;font-family:Raleway,Arimo,sans-serif;font-weight:300;font-size:27px;color:var(--ink)}
.section-title .dots{color:#999;font-size:16px;letter-spacing:2px;vertical-align:middle;margin:0 6px}

.cards{position:absolute;left:127px;display:flex;gap:11px}
.card{width:138px;height:202px;border:1px solid var(--line);position:relative;background:var(--white)}
.card-media{height:82px}
.card-label{position:absolute;left:10px;top:69px;width:118px;height:24px;background:var(--ink);color:var(--white);font-size:9px;display:flex;align-items:center;justify-content:center}
.card-text{position:absolute;left:9px;top:100px;width:120px;font-size:5.8px;line-height:10px;text-align:justify;color:var(--muted)}
.card-btn{position:absolute;left:40px;top:178px;width:56px;height:12px;border:1px solid #ccc;border-radius:6px;background:linear-gradient(#fafafa,#e4e4e4);font-size:6px;display:flex;align-items:center;justify-content:center;color:var(--ink)}

.m1{background:linear-gradient(#d9d9d9,#5a5a5a)}
.m2{background:linear-gradient(#cfcfcf,#8a8070)}
.m3{background:linear-gradient(#6fa2ad,#3a4c55)}
.m4{background:linear-gradient(#b0b0b0,#6a6a6a)}
.m5{background:linear-gradient(#ffffff,#dfe8f2)}
.m6{background:linear-gradient(#f4f4f4,#b8b39a)}
.m7{background:linear-gradient(#7c7c7c,#b59a88)}
.m8{background:linear-gradient(#e4e4e4,#c6c6c6)}

/* social */
.follow{position:absolute;top:1004px;width:160px;text-align:center}
.follow-ring{width:38px;height:38px;border-radius:50%;border:2.5px solid;margin:0 auto}
.follow-title{margin-top:10px;font-size:10px;color:var(--muted)}
.follow-title b{font-weight:700}
.follow-sub{font-size:7px;color:var(--muted);margin-top:2px}

.divider{position:absolute;left:127px;top:1111px;width:583px;border-top:1.5px dotted #999}
.footer-nav{position:absolute;left:0;top:1131px;width:837px;display:flex;justify-content:center;gap:8px;font-size:7px;color:var(--text)}
.footer-nav i{font-style:normal;font-size:6px}
.copyright{position:absolute;left:0;top:1154px;width:837px;text-align:center;font-size:7px;color:var(--ink)}
</style>
</head>
<body>

<header class="site-header">
  <div class="brand"><span class="brand-mark"></span><span class="brand-name">Torvane Capital</span></div>
  <div class="social-mini"><span>Friendlane</span><span>Circlenet</span><span>Streamvid</span></div>
  <div class="phone"><span class="phone-dot"></span>+00 - (0) 0000 000000</div>
  <div class="search"><span class="search-input">to search, type and hit enter</span><span class="search-btn">Search</span></div>
  <nav class="main-nav">
    <span class="active">Home</span><span>About Us</span><span>Services</span><span>Current Engagements</span><span>Completed Transactions</span><span>Contact Us</span>
  </nav>
</header>

<section class="hero">
  <div class="hero-map" role="img" aria-label="World map with flags of Canada, USA, China and Japan joined by flight arcs"></div>
  <div class="hero-arrow" style="left:127px"><svg width="8" height="10" viewBox="0 0 8 10"><path d="M6 1 2 5l4 4" stroke="#fff" stroke-width="1.5" fill="none"/></svg></div>
  <div class="hero-arrow" style="left:684px"><svg width="8" height="10" viewBox="0 0 8 10"><path d="M2 1l4 4-4 4" stroke="#fff" stroke-width="1.5" fill="none"/></svg></div>
  <h1 class="hero-title"><span class="l1">GLOBAL INVESTMENT</span><span class="l2">BANKING SERVICES</span></h1>
  <div class="hero-dots"><span class="on"></span><span></span><span></span></div>
</section>

<p class="intro">Torvane Capital is an independent investment bank working for buyers in a number of industries. We utilize exceptional technology in finding companies to meet our client's search criteria. We will not waste a buyer's time, a seller's time, or our own time.</p>

<h2 class="section-title" style="top:405px"><span class="dots">···</span>Who We Are<span class="dots">···</span></h2>
<div class="cards" style="top:466px">
  <article class="card"><div class="card-media m1" role="img" aria-label="Business team in suits"></div><div class="card-label">Our Name</div><p class="card-text">Lorem Ipsum is simply dummy text of the printing and typesetting industry. Lorem Ipsum has been the industry's standard dummy text ever since the 1500s, when an unknown printer took a galley of type and scrambled it to make a type specimen book.</p><div class="card-btn">Read More</div></article>
  <article class="card"><div class="card-media m2" role="img" aria-label="Two clients at a desk"></div><div class="card-label">Our Clients</div><p class="card-text">Lorem Ipsum is simply dummy text of the printing and typesetting industry. Lorem Ipsum has been the industry's standard dummy text ever since the 1500s, when an unknown printer took a galley of type and scrambled it to make a type specimen book.</p><div class="card-btn">Read More</div></article>
  <article class="card"><div class="card-media m3" role="img" aria-label="Businessman drawing a flowchart"></div><div class="card-label">Our Process</div><p class="card-text">Lorem Ipsum is simply dummy text of the printing and typesetting industry. Lorem Ipsum has been the industry's standard dummy text ever since the 1500s, when an unknown printer took a galley of type and scrambled it to make a type specimen book.</p><div class="card-btn">Read More</div></article>
  <article class="card"><div class="card-media m4" role="img" aria-label="Team building a rising red arrow"></div><div class="card-label">Team</div><p class="card-text">Lorem Ipsum is simply dummy text of the printing and typesetting industry. Lorem Ipsum has been the industry's standard dummy text ever since the 1500s, when an unknown printer took a galley of type and scrambled it to make a type specimen book.</p><div class="card-btn">Read More</div></article>
</div>

<h2 class="section-title" style="top:693px"><span class="dots">···</span>What We Do<span class="dots">···</span></h2>
<div class="cards" style="top:754px">
  <article class="card"><div class="card-media m5" role="img" aria-label="Dart in the centre of a target"></div><div class="card-label">Strategic Advisory</div><p class="card-text">Lorem Ipsum is simply dummy text of the printing and typesetting industry. Lorem Ipsum has been the industry's standard dummy text ever since the 1500s, when an unknown printer took a galley of type and scrambled it to make a type specimen book.</p><div class="card-btn">Read More</div></article>
  <article class="card"><div class="card-media m6" role="img" aria-label="Interlocking gears"></div><div class="card-label">Current Engagements</div><p class="card-text">Lorem Ipsum is simply dummy text of the printing and typesetting industry. Lorem Ipsum has been the industry's standard dummy text ever since the 1500s, when an unknown printer took a galley of type and scrambled it to make a type specimen book.</p><div class="card-btn">Read More</div></article>
  <article class="card"><div class="card-media m7" role="img" aria-label="Finger pressing a keyboard key"></div><div class="card-label">Completed Transactions</div><p class="card-text">Lorem Ipsum is simply dummy text of the printing and typesetting industry. Lorem Ipsum has been the industry's standard dummy text ever since the 1500s, when an unknown printer took a galley of type and scrambled it to make a type specimen book.</p><div class="card-btn">Read More</div></article>
  <article class="card"><div class="card-media m8" role="img" aria-label="Compliance sketch with rules and policies icons"></div><div class="card-label">Regulatory Compliance</div><p class="card-text">Lorem Ipsum is simply dummy text of the printing and typesetting industry. Lorem Ipsum has been the industry's standard dummy text ever since the 1500s, when an unknown printer took a galley of type and scrambled it to make a type specimen book.</p><div class="card-btn">Read More</div></article>
</div>

<div class="follow" style="left:171px"><div class="follow-ring" style="border-color:var(--friendlane)"></div><p class="follow-title">We're on <b style="color:var(--friendlane)">Friendlane</b></p><p class="follow-sub">Visit our Page</p></div>
<div class="follow" style="left:338px"><div class="follow-ring" style="border-color:var(--circlenet)"></div><p class="follow-title">We're on <b style="color:var(--circlenet)">Circlenet</b></p><p class="follow-sub">Visit our Page</p></div>
<div class="follow" style="left:501px"><div class="follow-ring" style="border-color:var(--streamvid)"></div><p class="follow-title">We're on <b style="color:var(--streamvid)">Streamvid</b></p><p class="follow-sub">Visit our Page</p></div>

<div class="divider"></div>
<nav class="footer-nav"><span>Home</span><i>●</i><span>About Us</span><i>●</i><span>Services</span><i>●</i><span>Current Engagements</span><i>●</i><span>Completed Transactions</span><i>●</i><span>Contact Us</span></nav>
<p class="copyright">© 2013 Torvane Capital</p>

</body>
</html>
```